Business Card Design Project

We require a professional business card designed for our consulting organisation that has the same theme and colours as our logo except for the grey.

Colours on the front should predominately be white however some reference to our logo colours except for the grey.

The back of the card should be have background colour that aligns with our logo colour.

Layout, style and design is up to the designer. So send through your designs

Details are attached in the word document project brief.

Target Market(s)

Target market are large corporate organisations

Industry/Entity Type

Business

Requirements
Must have
• Content on the front must have:

Dean Halvorsen
Managing Director

P: 0417 285 394
E: Dean@brevolinkpartners.com
W: www.brevolinkpartners.com

Content on the back must have the words:
Alliances
Placement
Training
Support

Design Colours
Must align to our logo

```html
<!DOCTYPE html>
<html lang="en">
<head>
<meta charset="utf-8">
<title>BrevoLink Partners – Business Cards</title>
<link href="https://fonts.googleapis.com/css2?family=Jost:wght@400;500&family=Lato:wght@700&display=swap" rel="stylesheet">
<style>
  :root {
    --brand-blue: #2191d1;
    --brand-blue-deep: #1a7fc0;
    --icon-teal: #1f9bc4;
    --paper: #ffffff;
    --page: #ffffff;
    --shadow: rgba(0, 0, 0, 0.28);
  }
  * { margin: 0; padding: 0; box-sizing: border-box; }
  html, body {
    width: 1197px;
    height: 1200px;
    overflow: hidden;
    background: var(--page);
  }
  .canvas {
    position: relative;
    width: 1197px;
    height: 1200px;
  }
  .card {
    position: absolute;
    width: 640px;
    height: 370px;
    overflow: hidden;
    box-shadow: 0 4px 12px var(--shadow);
  }

  /* Back of card */
  .card-back {
    left: 90px;
    top: 150px;
    background: var(--brand-blue);
    border-bottom-right-radius: 70px;
    color: var(--paper);
  }
  .card-back .brand {
    position: absolute;
    left: 0;
    right: 0;
    top: 120px;
    display: flex;
    align-items: center;
    justify-content: center;
    gap: 16px;
  }
  .brand-dot {
    width: 54px;
    height: 54px;
    border-radius: 50%;
    background: var(--paper);
    flex: none;
  }
  .brand-name {
    font-family: "Jost", sans-serif;
    font-weight: 500;
    font-size: 36px;
    line-height: 1;
    letter-spacing: 1px;
  }
  .services {
    position: absolute;
    left: 0;
    right: 0;
    top: 232px;
    display: flex;
    justify-content: center;
    gap: 30px;
    list-style: none;
    font-family: "Lato", sans-serif;
    font-weight: 700;
    font-size: 23px;
  }

  /* Front of card */
  .card-front {
    left: 467px;
    top: 650px;
    background: var(--paper);
    border-bottom-left-radius: 60px;
  }
  .card-front .wave {
    position: absolute;
    inset: 0;
  }
  .card-front .brand {
    position: absolute;
    right: 36px;
    top: 72px;
    display: flex;
    align-items: center;
    gap: 14px;
    color: var(--paper);
  }
  .card-front .brand-name { font-size: 34px; }
  .holder {
    position: absolute;
    left: 58px;
    top: 262px;
    font-family: "Jost", sans-serif;
    color: var(--brand-blue-deep);
    text-align: center;
  }
  .holder-name { font-size: 23px; font-weight: 400; }
  .holder-title { font-size: 20px; font-weight: 400; }
  .contacts {
    position: absolute;
    left: 300px;
    top: 262px;
    list-style: none;
    font-family: "Jost", sans-serif;
    font-size: 15px;
    color: var(--brand-blue-deep);
  }
  .contacts li {
    display: flex;
    align-items: center;
    gap: 26px;
    height: 34px;
  }
  .contact-icon {
    width: 26px;
    height: 26px;
    flex: none;
  }
</style>
</head>
<body>
<main class="canvas">

  <section class="card card-back" aria-label="Back of business card">
    <div class="brand">
      <span class="brand-dot"></span>
      <span class="brand-name">BrevoLink Partners</span>
    </div>
    <ul class="services">
      <li>Alliances</li>
      <li>Placement</li>
      <li>Training</li>
      <li>Support</li>
    </ul>
  </section>

  <section class="card card-front" aria-label="Front of business card">
    <svg class="wave" width="640" height="370" viewBox="0 0 640 370" aria-hidden="true">
      <path d="M0,0 H640 V272 C530,286 430,250 340,180 C250,112 120,108 0,124 Z" fill="var(--brand-blue)"/>
    </svg>

    <div class="brand">
      <span class="brand-dot"></span>
      <span class="brand-name">BrevoLink Partners</span>
    </div>

    <div class="holder">
      <p class="holder-name">Dean Halvorsen</p>
      <p class="holder-title">Managing Director</p>
    </div>

    <ul class="contacts">
      <li>
        <svg class="contact-icon" viewBox="0 0 26 26" aria-label="Phone">
          <circle cx="13" cy="13" r="13" fill="var(--icon-teal)"/>
          <path d="M8 9c1-2 3-2 3-1l1 2-1 1c1 2 2 3 4 4l1-1 2 1c1 0 1 2-1 3-4 1-10-5-9-9z" fill="#fff"/>
        </svg>
        <span>0417 285 394</span>
      </li>
      <li>
        <svg class="contact-icon" viewBox="0 0 26 26" aria-label="Email">
          <circle cx="13" cy="13" r="13" fill="var(--icon-teal)"/>
          <rect x="7" y="9" width="12" height="9" fill="#fff"/>
          <path d="M7 9l6 5 6-5" fill="none" stroke="var(--icon-teal)" stroke-width="1.2"/>
        </svg>
        <span>Dean@brevolinkpartners.com</span>
      </li>
      <li>
        <svg class="contact-icon" viewBox="0 0 26 26" aria-label="Website">
          <circle cx="13" cy="13" r="13" fill="var(--icon-teal)"/>
          <g fill="none" stroke="#fff" stroke-width="1.2">
            <circle cx="13" cy="13" r="7"/>
            <ellipse cx="13" cy="13" rx="3" ry="7"/>
            <path d="M6 13h14M7.5 9.5h11M7.5 16.5h11"/>
          </g>
        </svg>
        <span>www.brevolinkpartners.com</span>
      </li>
    </ul>
  </section>

</main>
</body>
</html>
```